Quenderil - Still Grace Cosmetics

Please design a logo and business cards for new food supplements, cosmetics and herbal fixatives. The products are produced ecologically and biologically in the South Tyrol and Trentino alps. The products are pure and noble. Quenderil = pure vitality Colors Background: dark or black matt (soft touch) Logodesign: powerful, elegant, violet with glossy foil The logo and design should convey warmth, passion and the 6th sense, you should get the impression that you can smell the herbal odor , Logo and business cards for new food supplements, cosmetics and herbal fixatives. The products are produced ecologically and biologically in the South Tyrol and Trentino alps. The products are pure and noble. Quenderil = pure vitality Colors Background: dark or black matt (softtouch) Logodesign: powerful elegant violet with glossy foil The logo and design is meant to convey warmth, passion and the 6th sense, you should get the impression that you can smell the herbal perfume.

Target Market(s)

Food, food supplements, vitality, health

Contact Information for Business Card

Please provide an elegant darf design that is puristic, but has a very good logo design
Elegantes dunkles design, puristisch

Logo Text

Quenderil - still Grace

Colors
6b449b

Requirements
Must have
• SVG Files Alpha channel for foil embossing High-quality design
Nice to have
• Pure elegance
Should not have
• to colorful colors

```html
<!DOCTYPE html>
<html lang="en">
<head>
<meta charset="utf-8">
<title>Quenderil – Business Cards</title>
<link rel="stylesheet" href="https://fonts.googleapis.com/css2?family=Source+Sans+3:wght@300;400;600;700&display=swap">
<style>
  :root {
    --page: #ecebe8;
    --card-dark: #1e1d22;
    --card-light: #ffffff;
    --brand-violet: #6b449b;
    --brand-violet-light: #a884d0;
    --violet-deep: #4e2f75;
    --ink: #2b2b2b;
    --ink-soft: #3d3d3d;
    --faint-violet: #f1ebf7;
    --shadow: 0 14px 30px rgba(0,0,0,.18);
  }
  * { box-sizing: border-box; margin: 0; padding: 0; }
  html, body { width: 1200px; height: 900px; overflow: hidden; }
  body {
    background: var(--page);
    font-family: "Source Sans 3", Arial, sans-serif;
    display: flex;
    align-items: center;
    justify-content: center;
    gap: 40px;
  }
  .card {
    position: relative;
    width: 525px;
    height: 300px;
    box-shadow: var(--shadow);
    overflow: hidden;
  }
  .card--back { background: var(--card-dark); display: flex; align-items: center; justify-content: center; }
  .card--front { background: var(--card-light); }

  .brand {
    display: flex;
    align-items: center;
    gap: 10px;
    font-weight: 300;
    letter-spacing: 4px;
    line-height: 1;
  }
  .brand__dot { border-radius: 50%; flex: none; }
  .card--back .brand { font-size: 56px; color: var(--brand-violet-light); }
  .card--back .brand__dot { width: 26px; height: 26px; background: var(--brand-violet-light); }

  .card--front .brand { position: absolute; left: 40px; top: 70px; font-size: 40px; letter-spacing: 3px; color: var(--brand-violet); }
  .card--front .brand__dot { width: 20px; height: 20px; background: var(--brand-violet); }

  .decor-circle {
    position: absolute;
    right: -60px;
    top: -50px;
    width: 240px;
    height: 240px;
    border-radius: 50%;
    background: var(--faint-violet);
  }

  .person { position: absolute; left: 44px; top: 140px; }
  .person__name { color: var(--brand-violet); font-weight: 700; font-size: 19px; letter-spacing: .3px; }
  .person__role { color: var(--ink-soft); font-size: 15px; margin-top: 1px; }

  .contacts { position: absolute; left: 44px; top: 198px; list-style: none; }
  .contacts li {
    display: flex; align-items: center; gap: 8px;
    font-size: 15px; color: var(--ink); line-height: 21px;
  }
  .contacts svg { width: 12px; height: 12px; fill: var(--brand-violet); flex: none; }

  .address {
    position: absolute; right: 26px; top: 222px;
    text-align: right; font-size: 12.5px; line-height: 17px; color: var(--ink);
    font-style: normal;
  }

  .band { position: absolute; left: 0; right: 0; bottom: 0; height: 12px; display: flex; }
  .band__primary { flex: 0 0 56%; background: var(--brand-violet); }
  .band__secondary { flex: 1; background: var(--brand-violet-light); }
</style>
</head>
<body>
  <section class="card card--back" aria-label="Business card back">
    <div class="brand"><span>Quenderil</span><span class="brand__dot"></span></div>
  </section>

  <section class="card card--front" aria-label="Business card front">
    <div class="decor-circle"></div>
    <div class="brand"><span>Quenderil</span><span class="brand__dot"></span></div>

    <div class="person">
      <p class="person__name">ELENA MARTELL</p>
      <p class="person__role">Managing Director</p>
    </div>

    <ul class="contacts">
      <li>
        <svg viewBox="0 0 24 24" aria-hidden="true"><path d="M6.6 10.8a15.1 15.1 0 0 0 6.6 6.6l2.2-2.2c.3-.3.7-.4 1-.2 1.1.4 2.3.6 3.6.6.6 0 1 .4 1 1V20c0 .6-.4 1-1 1C10.6 21 3 13.4 3 4c0-.6.4-1 1-1h3.5c.6 0 1 .4 1 1 0 1.3.2 2.5.6 3.6.1.3 0 .7-.2 1z"/></svg>
        (044)908172635
      </li>
      <li>
        <svg viewBox="0 0 24 24" aria-hidden="true"><path d="M2 5h20v14H2zM4 7v.4l8 5.2 8-5.2V7zm0 2.8V17h16V9.8l-8 5.2z"/></svg>
        info@quenderil-mail.com
      </li>
      <li>
        <svg viewBox="0 0 24 24" aria-hidden="true"><circle cx="12" cy="12" r="10"/></svg>
        www.quenderil-site.com
      </li>
    </ul>

    <address class="address">
      48, Larchwood Lane,<br>Alpenland, 39100
    </address>

    <div class="band"><span class="band__primary"></span><span class="band__secondary"></span></div>
  </section>
</body>
</html>
```